Carpet cleaning company wants business card

Need an exciting new fresh design for business cards for my carpet cleaning /pest control business
www.tidewellhomecare.com.au
Can design include a lined section for quoting or information? Thanks !

```html
<!DOCTYPE html>
<html lang="en">
<head>
<meta charset="utf-8">
<title>Tidewell Home Care – Business Card</title>
<link href="https://fonts.googleapis.com/css2?family=Outfit:wght@400;500;700;800&display=swap" rel="stylesheet">
<style>
  :root {
    --brand-blue: #0a58a6;
    --title-blue: #0b56a5;
    --accent-red: #ef3f3a;
    --paper: #ffffff;
    --board: #f5f5f5;
    --board-text: #ebeaea;
    --mesh-blue: #c9daf0;
    --rule-blue: #9bb9dd;
  }
  * { box-sizing: border-box; margin: 0; padding: 0; }
  html, body { width: 1200px; height: 660px; overflow: hidden; }
  body {
    position: relative;
    background: var(--board);
    font-family: "Outfit", sans-serif;
  }
  .backdrop-name {
    position: absolute;
    left: 10px;
    font-weight: 800;
    font-size: 210px;
    line-height: 1;
    color: var(--board-text);
    white-space: nowrap;
    letter-spacing: -4px;
  }
  .backdrop-name.top { top: -20px; }
  .backdrop-name.bottom { top: 370px; }
  .board-title {
    position: absolute;
    top: 34px; left: 0; width: 100%;
    text-align: center;
    font-size: 44px;
    font-weight: 700;
    color: var(--title-blue);
    letter-spacing: -0.5px;
  }
  .card {
    position: absolute;
    top: 140px;
    width: 510px;
    height: 330px;
    overflow: hidden;
    box-shadow: 0 28px 22px -14px rgba(0,0,0,0.35);
  }
  .card.front { left: 80px; background: var(--paper); }
  .card.back { left: 609px; background: var(--brand-blue); color: #fff; }
  .card-shapes { position: absolute; inset: 0; }
  .mesh { position: absolute; }
  .front .mesh.top-left {
    left: 0; top: 0; width: 285px; height: 92px;
    background: radial-gradient(ellipse at 50% 0%, var(--mesh-blue) 0%, rgba(201,218,240,0.4) 55%, rgba(255,255,255,0) 80%);
  }
  .front .mesh.bottom-right {
    right: 0; bottom: 0; width: 295px; height: 96px;
    background: radial-gradient(ellipse at 60% 100%, var(--mesh-blue) 0%, rgba(201,218,240,0.4) 55%, rgba(255,255,255,0) 80%);
  }
  .back .mesh.bottom-right {
    right: 0; bottom: 0; width: 160px; height: 128px;
    background: radial-gradient(ellipse at 100% 100%, rgba(47,182,232,0.65) 0%, rgba(47,182,232,0.25) 55%, rgba(10,88,166,0) 80%);
  }
  .front .brand-name {
    position: absolute;
    left: 0; width: 100%;
    top: 134px;
    text-align: center;
    color: var(--brand-blue);
    font-weight: 800;
    font-size: 36px;
    line-height: 1;
    letter-spacing: -0.5px;
  }
  .note-lines {
    position: absolute;
    left: 105px; top: 200px;
    width: 300px;
    list-style: none;
  }
  .note-lines li {
    height: 24px;
    border-bottom: 1px solid var(--rule-blue);
  }
  .back .brand-name {
    position: absolute;
    left: 42px; top: 34px;
    font-weight: 800;
    font-size: 36px;
    line-height: 1;
    letter-spacing: -0.5px;
  }
  .tagline {
    position: absolute;
    left: 42px; top: 89px;
    font-size: 19px;
    font-weight: 400;
  }
  .contact-heading {
    position: absolute;
    left: 42px; top: 144px;
    font-size: 20px;
    font-weight: 700;
  }
  .contact-heading::after {
    content: "";
    position: absolute;
    left: 1px; top: 30px;
    width: 135px; height: 4px;
    background: var(--accent-red);
  }
  .contact-list {
    position: absolute;
    left: 42px; top: 188px;
    list-style: none;
  }
  .contact-list li {
    display: flex;
    align-items: center;
    height: 18.5px;
    font-size: 15px;
    letter-spacing: 2px;
  }
  .contact-list svg { width: 15px; height: 15px; margin-right: 9px; flex: none; }
  .board-caption {
    position: absolute;
    top: 558px; left: 0; width: 100%;
    text-align: center;
    font-size: 28px;
    font-weight: 400;
    color: var(--title-blue);
  }
</style>
</head>
<body>
  <div class="backdrop-name top" aria-hidden="true">Tidewell</div>
  <div class="backdrop-name bottom" aria-hidden="true">Tidewell</div>

  <h1 class="board-title">BUSINESS CARD</h1>

  <section class="card front" aria-label="Card front">
    <div class="mesh top-left" role="img" aria-label="Fine blue wave-line mesh pattern"></div>
    <div class="mesh bottom-right" role="img" aria-label="Fine blue wave-line mesh pattern"></div>
    <svg class="card-shapes" viewBox="0 0 510 330" aria-hidden="true">
      <polygon points="468,0 510,0 510,42 429,66" fill="var(--accent-red)"/>
      <polygon points="0,290 76,265 39,330 0,330" fill="var(--accent-red)"/>
    </svg>
    <div class="brand-name">Tidewell Home Care</div>
    <ul class="note-lines" aria-label="Lined area for quotes and notes">
      <li></li><li></li><li></li>
    </ul>
  </section>

  <section class="card back" aria-label="Card back">
    <div class="mesh bottom-right" role="img" aria-label="Fine cyan wave-line mesh pattern"></div>
    <svg class="card-shapes" viewBox="0 0 510 330" aria-hidden="true">
      <polygon points="478,0 510,0 510,28 447,45" fill="var(--accent-red)"/>
      <polygon points="0,298 65,282 33,330 0,330" fill="var(--accent-red)"/>
    </svg>
    <div class="brand-name">Tidewell Home Care</div>
    <p class="tagline">Your Carpet Cleaning &amp; Pest Control Solution</p>
    <h2 class="contact-heading">Contact Us</h2>
    <ul class="contact-list">
      <li>
        <svg viewBox="0 0 16 16" fill="none" stroke="#fff" stroke-width="1.1"><path d="M4 1.5l2 3-1.3 1.3c.8 1.8 2.1 3.1 3.9 3.9L10 8.4l3 2-1 2.6c-5.5-.3-9.4-4.2-10.6-9.6z"/><path d="M9.5 2.5a4 4 0 0 1 4 4M9.5 4.5a2 2 0 0 1 2 2"/></svg>
        07 5550 1234
      </li>
      <li>
        <svg viewBox="0 0 16 16" fill="none" stroke="#fff" stroke-width="1.1"><path d="M4 1.5l2 3-1.3 1.3c.8 1.8 2.1 3.1 3.9 3.9L10 8.4l3 2-1 2.6c-5.5-.3-9.4-4.2-10.6-9.6z"/><path d="M9.5 2.5a4 4 0 0 1 4 4M9.5 4.5a2 2 0 0 1 2 2"/></svg>
        0400 555 219
      </li>
      <li>
        <svg viewBox="0 0 16 16" fill="none" stroke="#fff" stroke-width="1.1"><rect x="1" y="3.5" width="14" height="9"/><path d="M1 3.5l7 5.5 7-5.5M1 12.5l5-4.5M15 12.5l-5-4.5"/></svg>
        admin@tidewellhomecare.com.au
      </li>
      <li>
        <svg viewBox="0 0 16 16" fill="none" stroke="#fff" stroke-width="1.1"><circle cx="8" cy="8" r="6.5"/><ellipse cx="8" cy="8" rx="2.8" ry="6.5"/><path d="M1.5 8h13M2.5 4.8h11M2.5 11.2h11"/></svg>
        www.tidewellhomecare.com.au
      </li>
    </ul>
  </section>

  <p class="board-caption">Double-sided Business Card Measuring 8.5 Cm X 5.5 Cm</p>
</body>
</html>
```